Business Cards and label design needed!

I am a metalsmith, working in sterling silver, brass and moving slowly into adding some gold accent pieces. I also use patinas to add color to brass pieces. The peacock feather is used in my packaging, as both a label and tissue paper. I am attaching what I am currently using, and printing at home, but I need a design that I can have professionally printed. My website is www.fernhollowworks.com
Target Market(s)
Established Professionals, Independent thinkers, Art donors, Artist supporters
Industry/Entity Type
Jewelry
Contact Information for Business Card
I would like a business card with the basic contact information, including Facebook and Instagram. I currently use a peacock feather and would like to continue that. I like to use turquoise, Tiffany blue and colors in that direction. I am open to other suggestions. I would like to be able to transfer the design to oval labels as well.
Other font styles liked:
- Garamond or other fonts that have a slight script that is easy to read
Look and feel

```html
<!DOCTYPE html>
<html lang="en">
<head>
<meta charset="utf-8">
<title>Fern Hollow Works — Business Card</title>
<link rel="stylesheet" href="https://fonts.googleapis.com/css2?family=Petit+Formal+Script&family=Great+Vibes&family=Roboto:wght@400&display=swap">
<style>
  :root {
    --page-bg: #e9e6e2;
    --card-bg: #ffffff;
    --brand-indigo: #2e3192;
    --feather-teal: #1a9a9c;
    --feather-soft: #7fd0cf;
    --text-grey: #3c3c3c;
    --card-shadow: rgba(40, 30, 20, 0.22);
  }
  * { margin: 0; padding: 0; box-sizing: border-box; }
  html, body {
    width: 1200px;
    height: 886px;
    overflow: hidden;
    background: var(--page-bg);
  }
  .sheet {
    position: relative;
    width: 1200px;
    height: 886px;
  }
  .card {
    position: absolute;
    top: 294px;
    width: 520px;
    height: 297px;
    background: var(--card-bg);
    border-radius: 18px;
    box-shadow: 0 10px 28px var(--card-shadow);
    overflow: hidden;
  }
  .card--front { left: 50px; }
  .card--back { left: 630px; }

  /* Front: brand name */
  .brand {
    position: absolute;
    left: 0;
    right: 0;
    top: 128px;
    display: flex;
    align-items: center;
    justify-content: center;
    gap: 14px;
  }
  .brand__dot {
    width: 22px;
    height: 22px;
    border-radius: 50%;
    background: var(--feather-teal);
  }
  .brand__name {
    font-family: "Petit Formal Script", cursive;
    font-size: 30px;
    color: var(--brand-indigo);
    font-weight: 400;
    white-space: nowrap;
  }

  /* Back: contact */
  .contact {
    position: absolute;
    left: 280px;
    top: 62px;
    width: 220px;
  }
  .contact__mark {
    display: block;
    width: 60px;
    height: 40px;
    margin-left: 52px;
    border-radius: 50%;
    background: linear-gradient(100deg, var(--feather-soft), var(--feather-teal));
    opacity: 0.85;
  }
  .contact__name {
    font-family: "Great Vibes", cursive;
    font-size: 42px;
    line-height: 1.05;
    color: var(--feather-teal);
    font-weight: 400;
    margin: 4px 0 10px 18px;
    white-space: nowrap;
  }
  .contact__line {
    font-family: "Roboto", sans-serif;
    font-size: 12.5px;
    line-height: 1.45;
    color: var(--text-grey);
    white-space: nowrap;
  }
  .contact__line--gap { margin-top: 6px; }
</style>
</head>
<body>
  <main class="sheet">
    <section class="card card--front" aria-label="Card front">
      <div class="brand">
        <span class="brand__dot"></span>
        <span class="brand__name">Fern Hollow Works</span>
      </div>
    </section>

    <section class="card card--back" aria-label="Card back">
      <div class="contact">
        <span class="contact__mark" role="img" aria-label="Peacock feather motif"></span>
        <p class="contact__name">Marla Keene</p>
        <p class="contact__line">Cedar Bluff, TX 76012</p>
        <p class="contact__line contact__line--gap">940-555-0182</p>
        <p class="contact__line">hello@fernhollowworks.com</p>
        <p class="contact__line">www.fernhollowworks.com</p>
      </div>
    </section>
  </main>
</body>
</html>
```